Honey Label for 1kg square jar

We require premium looking honey label for 1kg packed in dark amber jar as shown in the image.
Brand is called :"Velmora Honey" - logo to be provided
We would like the following colours to be considered (white, gold and red)
We like to have some flowers and beehives on the background.
The label covers 3 sides of the square jar and were hoping to see render of the front side which should include the brand and also the words" 100% Premium Australian Honey"

Need extra days to review

```html
<!DOCTYPE html>
<html lang="en">
<head>
<meta charset="utf-8">
<title>Velmora Honey – Front Label</title>
<link rel="stylesheet" href="https://fonts.googleapis.com/css2?family=Questrial&display=swap">
<style>
  :root {
    --canvas: #ffffff;
    --label-top: #5a1418;
    --label-mid: #9c4a22;
    --label-bottom: #dc8c31;
    --text-light: #ffffff;
    --gold: #e8c15a;
    --comb-tone: rgba(196, 98, 38, 0.42);
    --comb-fade: rgba(196, 98, 38, 0);
    --flower-tone: rgba(150, 78, 28, 0.34);
    --flower-fade: rgba(150, 78, 28, 0);
  }
  * { margin: 0; padding: 0; box-sizing: border-box; }
  html, body {
    width: 1200px;
    height: 1200px;
    overflow: hidden;
    background: var(--canvas);
  }
  .canvas {
    position: relative;
    width: 1200px;
    height: 1200px;
    background: var(--canvas);
  }
  .label {
    position: absolute;
    left: 0;
    top: 400px;
    width: 1200px;
    height: 400px;
    overflow: hidden;
    background: linear-gradient(180deg, var(--label-top) 0%, var(--label-mid) 50%, var(--label-bottom) 100%);
  }
  .label__comb {
    position: absolute;
    top: 0;
    width: 392px;
    height: 250px;
  }
  .label__comb--left {
    left: 0;
    background: linear-gradient(180deg, var(--comb-tone) 0%, var(--comb-tone) 55%, var(--comb-fade) 100%);
    -webkit-mask: linear-gradient(90deg, #000 85%, transparent 100%);
            mask: linear-gradient(90deg, #000 85%, transparent 100%);
  }
  .label__comb--right {
    right: 0;
    background: linear-gradient(180deg, var(--comb-tone) 0%, var(--comb-tone) 55%, var(--comb-fade) 100%);
    -webkit-mask: linear-gradient(270deg, #000 85%, transparent 100%);
            mask: linear-gradient(270deg, #000 85%, transparent 100%);
  }
  .label__flowers {
    position: absolute;
    top: 150px;
    width: 320px;
    height: 250px;
    border-radius: 50%;
    background: radial-gradient(ellipse at center, var(--flower-tone) 0%, var(--flower-tone) 35%, var(--flower-fade) 72%);
  }
  .label__flowers--left { left: 180px; }
  .label__flowers--center-left { left: 380px; top: 170px; width: 200px; }
  .label__flowers--center-right { left: 690px; top: 170px; width: 200px; }
  .label__flowers--right { left: 720px; width: 320px; }
  .label__emblem {
    position: absolute;
    left: 50%;
    top: 70px;
    transform: translateX(-50%);
  }
  .label__brand {
    position: absolute;
    left: 0;
    right: 0;
    top: 115px;
    text-align: center;
    font-family: "Questrial", sans-serif;
    font-weight: 400;
    color: var(--text-light);
    font-size: 70px;
    line-height: 82px;
    letter-spacing: 1px;
    -webkit-text-stroke: 1.4px var(--text-light);
  }
  .label__tagline {
    position: absolute;
    left: 0;
    right: 0;
    top: 339px;
    text-align: center;
    font-family: "Questrial", sans-serif;
    color: var(--text-light);
    font-size: 18px;
    letter-spacing: 0.4px;
    -webkit-text-stroke: 0.3px var(--text-light);
  }
</style>
</head>
<body>
  <main class="canvas">
    <section class="label">
      <div class="label__comb label__comb--left" role="img" aria-label="Honeycomb beehive pattern"></div>
      <div class="label__comb label__comb--right" role="img" aria-label="Honeycomb beehive pattern"></div>
      <div class="label__flowers label__flowers--left" role="img" aria-label="Line-drawn blossom flowers"></div>
      <div class="label__flowers label__flowers--center-left" role="img" aria-label="Line-drawn blossom flowers"></div>
      <div class="label__flowers label__flowers--center-right" role="img" aria-label="Line-drawn blossom flowers"></div>
      <div class="label__flowers label__flowers--right" role="img" aria-label="Line-drawn blossom flowers"></div>
      <svg class="label__emblem" width="28" height="28" viewBox="0 0 28 28" role="img" aria-label="Gold bee emblem">
        <circle cx="14" cy="14" r="11" fill="var(--gold)"/>
      </svg>
      <h1 class="label__brand">VELMORA<br>HONEY</h1>
      <p class="label__tagline">100% Premium Australian Honey</p>
    </section>
  </main>
</body>
</html>
```